Stationery Design needed for logo design project

This project is linked to Professional LED lighting company needs a logo.

Our company needs a Stationery Design. Please refer to our original project in the link above.

```html
<!DOCTYPE html>
<html lang="en">
<head>
<meta charset="utf-8">
<title>Lumora Lighting – Business Card</title>
<link rel="stylesheet" href="https://fonts.googleapis.com/css2?family=Open+Sans:wght@400;600;700&display=swap">
<style>
  :root {
    --backdrop: #3a8f98;
    --card: #ffffff;
    --crimson: #c8173f;
    --crimson-deep: #a9142e;
    --violet: #6a5a99;
    --ink: #2b2b33;
    --ink-soft: #4a4a55;
  }
  * { margin: 0; padding: 0; box-sizing: border-box; }
  html, body { width: 1200px; height: 900px; overflow: hidden; }
  body {
    background: var(--backdrop);
    font-family: "Open Sans", Arial, sans-serif;
    position: relative;
  }
  .card {
    position: absolute;
    left: 250px;
    width: 700px;
    height: 400px;
    background: var(--card);
    overflow: hidden;
    box-shadow: 0 6px 18px rgba(0,0,0,0.18);
  }
  .card--back { top: 40px; }
  .card--front { top: 470px; }

  .band { position: absolute; }
  .card--back .band--left  { left: 0; top: 150px; width: 84px; height: 250px; background: var(--crimson); }
  .card--back .band--right { right: 0; top: 0; width: 64px; height: 200px; background: var(--crimson); }
  .card--front .band--left  { left: 0; top: 190px; width: 96px; height: 210px; background: var(--crimson-deep); }
  .card--front .band--right { right: 0; top: 0; width: 96px; height: 200px; background: var(--crimson-deep); }

  .brand {
    position: absolute;
    display: flex;
    align-items: center;
    gap: 8px;
  }
  .brand__mark { width: 14px; height: 14px; background: var(--violet); }
  .brand__name { font-weight: 700; font-size: 15px; color: var(--violet); white-space: nowrap; }
  .card--back .brand { left: 240px; top: 185px; }
  .card--front .brand { left: 120px; top: 180px; }

  .person {
    position: absolute;
    left: 360px;
    top: 70px;
  }
  .person__name { font-size: 34px; font-weight: 400; color: var(--ink); letter-spacing: 0.5px; }
  .person__title { font-size: 16px; color: var(--ink-soft); margin-top: 2px; }

  .contact {
    position: absolute;
    left: 360px;
    top: 170px;
    list-style: none;
  }
  .contact__item {
    display: flex;
    align-items: flex-start;
    gap: 12px;
    font-size: 13px;
    line-height: 17px;
    color: var(--ink-soft);
    margin-bottom: 10px;
  }
  .contact__icon { width: 20px; height: 20px; flex: none; }
</style>
</head>
<body>

  <section class="card card--back" aria-label="Business card back">
    <div class="band band--left"></div>
    <div class="band band--right"></div>
    <div class="brand">
      <span class="brand__mark"></span>
      <span class="brand__name">Lumora Lighting</span>
    </div>
  </section>

  <section class="card card--front" aria-label="Business card front">
    <div class="band band--left"></div>
    <div class="band band--right"></div>
    <div class="brand">
      <span class="brand__mark"></span>
      <span class="brand__name">Lumora Lighting</span>
    </div>

    <div class="person">
      <h1 class="person__name">D.K. Linwood</h1>
      <p class="person__title">Executive Director</p>
    </div>

    <ul class="contact">
      <li class="contact__item">
        <svg class="contact__icon" viewBox="0 0 20 20" aria-hidden="true">
          <circle cx="10" cy="10" r="10" fill="var(--violet)"/>
          <path d="M10 4a4 4 0 0 0-4 4c0 3 4 8 4 8s4-5 4-8a4 4 0 0 0-4-4z" fill="#fff"/>
          <circle cx="10" cy="8" r="1.6" fill="var(--violet)"/>
        </svg>
        <span>House no-12, Road no-04<br>Elm Park, Northfield - 4120</span>
      </li>
      <li class="contact__item">
        <svg class="contact__icon" viewBox="0 0 20 20" aria-hidden="true">
          <rect width="20" height="20" rx="3" fill="var(--violet)"/>
          <path d="M6 4.5l2.5 0 1 3-1.5 1.2a8 8 0 0 0 3.3 3.3l1.2-1.5 3 1v2.5c0 .6-.5 1-1 1A10 10 0 0 1 5 5.5c0-.5.4-1 1-1z" fill="#fff"/>
        </svg>
        <span>+44 0192 48810</span>
      </li>
      <li class="contact__item">
        <svg class="contact__icon" viewBox="0 0 20 20" aria-hidden="true">
          <rect width="20" height="20" rx="3" fill="var(--violet)"/>
          <rect x="4" y="6" width="12" height="8" fill="#fff"/>
          <path d="M4 6l6 5 6-5" fill="none" stroke="var(--violet)" stroke-width="1.3"/>
        </svg>
        <span>mail@lumoralight.com</span>
      </li>
      <li class="contact__item">
        <svg class="contact__icon" viewBox="0 0 20 20" aria-hidden="true">
          <circle cx="10" cy="10" r="10" fill="var(--violet)"/>
          <circle cx="10" cy="10" r="6" fill="none" stroke="#fff" stroke-width="1.3"/>
          <ellipse cx="10" cy="10" rx="2.6" ry="6" fill="none" stroke="#fff" stroke-width="1.1"/>
          <path d="M4 10h12" stroke="#fff" stroke-width="1.1"/>
        </svg>
        <span>http://www.lumoralight.com</span>
      </li>
    </ul>
  </section>

</body>
</html>
```